Digitale Weihnachtskarte für Energieberater
Zielgruppe
Beratung in Bezug auf Energiemanagement/Energieeffizienz in Gebäuden
Gebäudetechnik
Kunden aufzeigen, wie Energie und somit Kosten gespart werden können
Zielgruppe: unsere Kunden, Interessenten und Lieferanten
Aufgabenstellung
Die digitale Weihnachtskarte wird schlussendlich per Mailing verschickt. Es wird eine jpg- und eine pdf-Datei benötigt.
Design:
Weihnachtliches, eher schlichtes Design. Letztjährige Projekte: #293721, #484192, #437447
Logo muss integriert werden, muss aber nicht im Vordergrund stehen.
Das Bild im Anhang kann, aber muss nicht verwendet werden.
Farbwahl:
Blau:
CMYK = 95/75/0/0
HEX = #244a9a
RGB = 36/74/154
Orange:
CMYK = 0/60/100/0
HEX = #ef7d00
RGB = 239/125/0
Grau:
CMYK = 0/0/0/65
HEX = #7c7c7b
RGB = 124/124/123
Grün:
CMYK = 60/100/0/0
HEX = #76b82a
RGB = 118/184/42
Schrift: DIN oder Arial, nicht kursiv
Geschätzte Kunden und Partner
Das Jahr neigt sich dem Ende zu und lädt uns dazu ein, auf das vergangene Jahr zurückzublicken, aber auch mit Zuversicht und frischem Elan in einen neuen Zeitabschnitt zu starten. Dank fortschrittlichen Technologien, Prozessoptimierungen und Investitionen wurde der Erfolg der vendralis Schweiz AG vorangetrieben. Mit unserem neuen Standort in Stuttgart haben wir einen weiteren Meilenstein gelegt.
Dankbar dafür, dass wir mit Ihnen zusammen in die Zukunft weiterschreiten dürfen, wünschen wir Ihnen und Ihrer Familie eine entspannte und besinnliche Weihnachtszeit und ein glückliches neues Jahr!

```html
<!DOCTYPE html>
<html lang="de">
<head>
<meta charset="utf-8">
<title>Weihnachtskarte vendralis</title>
<link rel="stylesheet" href="https://fonts.googleapis.com/css2?family=Arimo:wght@400&family=Great+Vibes&display=swap">
<style>
  :root {
    --page-bg: #f3f3f3;
    --brand-blue: #244a9a;
    --night-deep: #070b2e;
    --night-mid: #0d2a8a;
    --glow-blue: #2f8cff;
    --glow-light: #bfe4ff;
    --violet: #4a2350;
    --text-light: #ffffff;
    --text-dark: #222222;
    --footer-bg: #ffffff;
  }
  html, body {
    margin: 0;
    padding: 0;
    width: 900px;
    height: 1200px;
    overflow: hidden;
    background: var(--page-bg);
  }
  .card {
    position: absolute;
    left: 34px;
    top: 147px;
    width: 819px;
    height: 939px;
    box-shadow: 0 1px 4px rgba(0,0,0,0.25);
    font-family: "Arimo", Arial, sans-serif;
  }
  .hero {
    position: relative;
    height: 424px;
    overflow: hidden;
  }
  .hero-art {
    position: absolute;
    inset: 0;
    background:
      radial-gradient(circle at 52% 48%, var(--glow-light) 0%, var(--glow-blue) 8%, rgba(47,140,255,0.35) 22%, transparent 45%),
      radial-gradient(ellipse at 100% 0%, var(--violet) 0%, transparent 35%),
      radial-gradient(ellipse at 78% 55%, #1747b8 0%, var(--night-deep) 70%),
      linear-gradient(90deg, var(--night-deep) 0%, var(--night-mid) 45%, var(--night-deep) 100%);
    background-blend-mode: screen, normal, normal, normal;
  }
  .greeting-script {
    position: absolute;
    margin: 0;
    color: var(--text-light);
    font-family: "Great Vibes", cursive;
    font-weight: 400;
    line-height: 1;
    white-space: nowrap;
  }
  .script-frohe { left: 114px; top: 118px; font-size: 62px; }
  .script-weihnachten { left: 56px; top: 188px; font-size: 62px; }
  .script-gutes { left: 138px; top: 248px; font-size: 34px; }
  .script-jahr { left: 120px; top: 282px; font-size: 42px; }

  .message {
    background: var(--brand-blue);
    height: 425px;
    box-sizing: border-box;
    padding: 66px 26px 0 46px;
    color: var(--text-light);
    font-size: 19px;
    line-height: 23px;
  }
  .message p { margin: 0 0 23px; }
  .message .salutation { margin-bottom: 23px; }

  .footer {
    position: relative;
    background: var(--footer-bg);
    height: 90px;
    color: var(--text-dark);
    font-size: 12px;
    line-height: 14px;
  }
  .brand {
    position: absolute;
    left: 44px;
    top: 24px;
    display: flex;
    align-items: center;
    gap: 10px;
    color: var(--brand-blue);
    font-size: 24px;
  }
  .brand-dot {
    width: 24px;
    height: 24px;
    border-radius: 50%;
    background: var(--brand-blue);
  }
  .address {
    position: absolute;
    top: 17px;
    margin: 0;
    font-style: normal;
  }
  .address-ch { left: 264px; }
  .address-de { left: 438px; }
  .web {
    position: absolute;
    left: 678px;
    top: 57px;
  }
</style>
</head>
<body>
  <main class="card">
    <section class="hero">
      <div class="hero-art" role="img" aria-label="Leuchtende blaue Weltkugel aus Lichtlinien und Sternpunkten vor dunkelblauem Nachthimmel mit Schneeflocken"></div>
      <h1 class="greeting-script script-frohe">Frohe</h1>
      <p class="greeting-script script-weihnachten">Weihnachten</p>
      <p class="greeting-script script-gutes">und ein gutes</p>
      <p class="greeting-script script-jahr">Neues Jahr</p>
    </section>

    <section class="message">
      <p class="salutation">Geschätzte Kunden und Partner</p>
      <p>Das Jahr neigt sich dem Ende zu und lädt uns dazu ein, auf das vergangene Jahr zu&shy;rückzublicken, aber auch mit Zuversicht und frischem Elan in einen neuen Zeitabschnitt zu starten. Dank fortschrittlichen Technologien, Prozessoptimierungen und Investitionen wurde der Erfolg der vendralis Schweiz AG vorangetrieben. Mit unserem neuen Stan&shy;dort in Stuttgart haben wir einen weiteren Meilenstein gelegt.</p>
      <p>Dankbar dafür, dass wir mit Ihnen zusammen in die Zukunft weiterschreiten dürfen, wünschen wir Ihnen und Ihrer Familie eine entspannte und besinnliche Weihnachtszeit und ein glückliches neues Jahr!</p>
      <p>Ihr vendralis-Team</p>
    </section>

    <footer class="footer">
      <div class="brand"><span class="brand-name">vendralis</span><span class="brand-dot"></span></div>
      <address class="address address-ch">vendralis Schweiz AG<br>Lindenweg 14<br>4600 Olten<br>Tel. +41 62 000 11 22</address>
      <address class="address address-de">vendralis Schweiz AG<br>Niederlassung Deutschland<br>Werkstrasse 9, 70565 Stuttgart<br>Tel. +49 711 00000 123</address>
      <span class="web">www.vendralis.com</span>
    </footer>
  </main>
</body>
</html>
```